依頼詳細
現在、お店のロゴはあります。既存のロゴを使用して、立て看板を新しくしたいと思っています。看板の入稿に必要なデザインをillustratorで作成して頂きたいと思います。
重視するポイントは、
1。概要、特徴にも記載しましたが2Fとわかること。
2.ワインはそうですが、お食事ができること。
3.現在使用しているロゴを看板の中心にもっていってワインと一目でわかるようにしたい
4.現在の立て看板がとてもカジュアルな為、店内の雰囲気とかなりギャップがあります。若年の方が立ち飲みバルや、居酒屋、カフェ等と間違えて誤って入ってこられることがたまにあります。お店の雰囲気がでるようなシンプルで雰囲気のあるデザインを希望します。看板製作会社が、完全データの支給を要求しているため、Adobe Illustratorアウトラインデータ Mac=8.0 Win=CSにて納品お願いします。
お店の雰囲気、現在の看板、ロゴなどは添付ファイル参照ください。
記載項目
店舗名、2F、ワインとお食事、今のロゴ。定番メニューのリスト、電話番号。席数。
希望イメージ
シンプル 複雑
単色 カラフル
暗い 明るい
日常 高級
遊び心 厳粛
未来的 伝統的
女性的 男性的
希望する色
白、ワインレッド系、ロゴに合わせたカラー
納品ファイル
• 高解像度JPG (.jpg)
• イラストレーター形式 (.ai)
補足説明
入口の間口が狭いために、看板に必ず2F+↑を記載していただきたいです。表、左上がり、裏、右上がりの☝をつけてほしいです。現在の立て看板ファイルを参照してください。
看板仕上がりサイズはW600×H900です。【画面有効サイズ】 W530×H830mmとなっています。内側に投光機を設置し、ライトアップされます。宜しくお願いいたします。
■ 選んだ理由

現在の問題点をクリアし、お店の雰囲気が看板一つで出ている所。

■ 提案者全員のお礼・コメント

修正等にご対応いただきまして誠にありがとうございました。今後も名刺の修正等依頼していくつもりですので機会がありましたら是非とも宜しくお願いいたします。

```html
<!DOCTYPE html>
<html lang="ja">
<head>
<meta charset="utf-8">
<title>ALCOVE — Wine &amp; Dine 2F</title>
<link rel="stylesheet" href="https://fonts.googleapis.com/css2?family=Shippori+Mincho:wght@400;500&family=Noto+Serif+JP:wght@400;500;600&family=Josefin+Sans:wght@400;600&display=swap">
<style>
  :root {
    --paper: #fdfaf3;
    --wine: #c41e2a;
    --brown: #5b2d1c;
    --white: #ffffff;
  }
  * { margin: 0; padding: 0; box-sizing: border-box; }
  html, body { width: 794px; height: 1200px; overflow: hidden; background: var(--paper); }
  .board { position: relative; width: 794px; height: 1200px; background: var(--paper); overflow: hidden; }
  .stairs { position: absolute; inset: 0; }
  .floor {
    position: absolute; left: 548px; top: 80px;
    font-family: "Noto Serif JP", serif; font-weight: 500;
    font-size: 150px; line-height: 1; color: var(--white); letter-spacing: -4px;
  }
  .tagline-vertical {
    position: absolute; left: 24px; top: 190px;
    writing-mode: vertical-rl;
    font-family: "Shippori Mincho", serif; font-weight: 400;
    font-size: 80px; line-height: 1; letter-spacing: 6px; color: var(--brown);
  }
  .brand-mark {
    position: absolute; left: 176px; top: 500px;
    width: 110px; height: 110px; border-radius: 50%; background: var(--wine);
  }
  .brand { position: absolute; left: 300px; top: 492px; width: 340px; text-align: right; }
  .brand-kind {
    font-family: "Josefin Sans", sans-serif; font-size: 32px; color: var(--wine);
    letter-spacing: 1px; line-height: 1; padding-right: 16px;
  }
  .brand-name {
    font-family: "Josefin Sans", sans-serif; font-weight: 600;
    font-size: 94px; line-height: 1; color: var(--brown); letter-spacing: 0;
    margin-top: 10px;
  }
  .phone {
    font-family: "Noto Serif JP", serif; font-size: 32px; color: var(--brown);
    margin-top: 10px; letter-spacing: 1px; padding-right: 16px;
  }
  .menu {
    position: absolute; left: 190px; top: 728px; width: 460px;
    font-family: "Noto Serif JP", serif; font-size: 24px; color: var(--brown);
    list-style: none;
  }
  .menu li { display: flex; height: 34px; align-items: center; }
  .menu .item { width: 282px; }
  .menu.dishes { top: 960px; }
  .seats {
    position: absolute; left: 145px; top: 1062px; width: 485px; height: 44px;
    border-radius: 22px; background: var(--brown); color: var(--paper);
    font-family: "Noto Serif JP", serif; font-size: 22px;
    display: flex; align-items: center; justify-content: center; letter-spacing: 2px;
  }
</style>
</head>
<body>
<main class="board">
  <svg class="stairs" width="794" height="1200" viewBox="0 0 794 1200" aria-hidden="true">
    <polygon fill="var(--wine)" points="0,0 794,0 794,250 460,250 460,205 370,205 370,160 290,160 290,120 210,120 210,80 130,80 130,40 0,40"/>
    <g class="arrow-up-left" fill="var(--white)">
      <polygon points="488,42 540,50 525,62 560,97 548,109 513,74 500,89"/>
    </g>
  </svg>
  <div class="floor">2F</div>

  <h2 class="tagline-vertical">食事のできるワインバー</h2>

  <div class="brand-mark" aria-hidden="true"></div>
  <header class="brand">
    <div class="brand-kind">WINE &amp; DINE</div>
    <h1 class="brand-name">ALCOVE</h1>
    <div class="phone">03-5550-0142</div>
  </header>

  <ul class="menu drinks">
    <li><span class="item">Glass Wine</span><span class="price">￥900～</span></li>
    <li><span class="item">Glass Champagne</span><span class="price">￥1,400～</span></li>
    <li><span class="item">BTL Wine</span><span class="price">￥5,000～</span></li>
    <li><span class="item">BTL Champagne</span><span class="price">￥8,500～</span></li>
    <li><span class="item">Glass Wine</span><span class="price">￥900～</span></li>
    <li><span class="item">Glass Champagne</span><span class="price">￥1,400～</span></li>
  </ul>

  <ul class="menu dishes">
    <li><span class="item">鯛のカルパッチョ</span><span class="price">￥2,000～</span></li>
    <li><span class="item">ホロホロ鳥の香草焼き</span><span class="price">￥2,500～</span></li>
  </ul>

  <div class="seats">カウンター５席　テーブル５席</div>
</main>
</body>
</html>
```